Powerpoint template for Trivia Company

Revamp of our current powerpoint template to make it more professional and fun for the players. Something worthy of a trivia company. Please see logo attached for potential colour - but also open to other ideas.

NO BRANDING REQUIRED (IE: No mention of our company or logo on the template please)

Target Market(s)

Bars/restaurants

Colors
3176b5
00a990

```html
<!DOCTYPE html>
<html lang="en">
<head>
<meta charset="utf-8">
<title>Welcome to Trivia Night</title>
<link rel="stylesheet" href="https://fonts.googleapis.com/css2?family=Open+Sans:wght@400;500&display=swap">
<style>
  :root {
    --brand-blue: #3176b5;
    --brand-green: #00a990;
    --mint: #7fe8c8;
    --aqua: #34ddd0;
    --teal: #14c6cc;
    --ocean: #0aa6d0;
    --deep-blue: #1b6fd0;
    --title-white: #ffffff;
  }
  * { margin: 0; padding: 0; box-sizing: border-box; }
  html, body {
    width: 1200px;
    height: 675px;
    overflow: hidden;
    background: #ffffff;
  }
  .slide {
    position: relative;
    width: 1200px;
    height: 675px;
    overflow: hidden;
    font-family: "Open Sans", sans-serif;
  }
  .pattern-band {
    position: absolute;
    left: 0;
    width: 100%;
  }
  .pattern-band--top {
    top: 0;
    height: 109px;
    background: linear-gradient(100deg, var(--mint) 0%, var(--aqua) 45%, var(--teal) 100%);
  }
  .pattern-band--bottom {
    top: 540px;
    height: 135px;
    background:
      linear-gradient(180deg, rgba(255,255,255,0) 80%, var(--deep-blue) 100%),
      linear-gradient(100deg, var(--aqua) 0%, var(--teal) 45%, var(--ocean) 100%);
  }
  .accent-rule {
    position: absolute;
    top: 109px;
    left: 0;
    width: 100%;
    height: 12px;
    background: var(--brand-green);
  }
  .title-panel {
    position: absolute;
    top: 121px;
    left: 0;
    width: 100%;
    height: 419px;
    background: var(--brand-blue);
    display: flex;
    align-items: center;
    justify-content: center;
  }
  .slide-title {
    color: var(--title-white);
    font-weight: 500;
    font-size: 112px;
    line-height: 143px;
    letter-spacing: 3px;
    text-align: center;
    text-transform: uppercase;
    text-shadow:
      1px 1px 0 rgba(200, 210, 225, 0.9),
      5px 7px 8px rgba(10, 30, 60, 0.55);
    margin-top: 6px;
  }
</style>
</head>
<body>
  <main class="slide">
    <div class="pattern-band pattern-band--top" role="img" aria-label="Low-poly geometric pattern in mint and teal tones"></div>
    <div class="accent-rule"></div>
    <section class="title-panel">
      <h1 class="slide-title">Welcome to<br>Trivia Night!</h1>
    </section>
    <div class="pattern-band pattern-band--bottom" role="img" aria-label="Low-poly geometric pattern in aqua and ocean blue tones"></div>
  </main>
</body>
</html>
```